Catchy Cards for Hospital

I run a rural hospital in Texas called Pellor Valley Hospital and am in need of contemporary business cards for all of my Department Heads. While our logo is somewhat simplistic, I don't have the option of changing it at this time, so anything to make the rest of the card present the appearance of a modern, professional healthcare facility would be great. Although the attached files are in black, our hospital colors are in a copper brown and black. I need to be able to change the name and title on the card so I can get cards printed for various department heads.

Target Market(s)

Referring physicians, large hospital systems, national organizations, state and federal government

Industry/Entity Type

Hospital

Contact Information for Business Card

Name Dale Hoskin
Title CEO

Phone: Main 555-555-0147 & Direct xxxxxx
Fax xxxxx
dale.hoskin@pellorvh.example
382 Wimble Street Box 415
Ambermoor, Westland 76902

Font styles to use
Serif

Colors
f48340

Requirements
Must have
• Clean crisp lines and ability to modify names, titles and emails
• On the back "PellorValleyHospital.Example
Nice to have
• Needs to be in line with logo, which is a bit dated and not too appealing, but I'm hoping that the rest of the card can make up for that fact just a little bit.
• Hospital's colors are a copper brown, black and white
Should not have
• Shapes or anything distracting

```html
<!DOCTYPE html>
<html lang="en">
<head>
<meta charset="utf-8">
<title>Pellor Valley Hospital – Business Card</title>
<link href="https://fonts.googleapis.com/css2?family=Roboto:wght@400;700&family=Roboto+Condensed:wght@700&display=swap" rel="stylesheet">
<style>
  :root {
    --backdrop: #5b4939;
    --ink: #000000;
    --paper: #f3f3f3;
    --text: #4a4a4a;
    --muted: #a8a8a8;
    --reverse: #ffffff;
  }
  * { margin: 0; padding: 0; box-sizing: border-box; }
  html, body {
    width: 1200px; height: 960px; overflow: hidden;
    background: var(--backdrop);
    font-family: "Roboto", Arial, sans-serif;
  }
  .card {
    position: absolute;
    width: 600px; height: 343px;
  }
  .card-front { left: 314px; top: 113px; background: var(--paper); }
  .card-back { left: 311px; top: 472px; background: var(--ink); }

  .front-band {
    position: absolute; left: 0; top: 0;
    width: 72px; height: 100%;
    background: var(--ink);
  }
  .wordmark {
    position: absolute;
    font-weight: 700;
  }
  .card-front .wordmark {
    left: 88px; top: 27px;
    font-size: 40px;
    line-height: 45px;
    color: var(--ink);
  }
  .card-back .wordmark {
    left: 0; right: 0; top: 93px;
    text-align: center;
    font-size: 44px;
    line-height: 52px;
    color: var(--reverse);
  }

  .contact-block {
    position: absolute; right: 27px; top: 139px;
    text-align: right;
    color: var(--text);
    font-size: 14.5px;
  }
  .person-name {
    font-family: "Roboto Condensed", "Roboto", sans-serif;
    font-weight: 700;
    font-size: 21px;
    color: var(--ink);
    line-height: 24px;
  }
  .person-title {
    color: var(--muted);
    font-size: 14.5px;
    line-height: 20px;
    margin-bottom: 14px;
  }
  .address { line-height: 18px; margin-bottom: 8px; }
  .contact-list { list-style: none; }
  .contact-list li {
    display: flex; justify-content: flex-end; align-items: center;
    line-height: 19px;
  }
  .contact-list svg {
    width: 13px; height: 13px;
    margin-left: 9px;
    fill: var(--ink);
  }
  .back-url {
    position: absolute; left: 0; right: 0; top: 290px;
    text-align: center;
    color: var(--reverse);
    font-weight: 700;
    font-size: 14.5px;
  }
</style>
</head>
<body>
  <section class="card card-front">
    <div class="front-band"></div>
    <div class="wordmark">Pellor<br>Valley<br>Hospital</div>
    <div class="contact-block">
      <p class="person-name">DALE HOSKIN</p>
      <p class="person-title">CEO</p>
      <p class="address">382 Wimble Street Box 415<br>Ambermoor, Westland 76902</p>
      <ul class="contact-list">
        <li>555-555-0147
          <svg viewBox="0 0 16 16" aria-hidden="true"><path d="M3.6 1.2l2.2 2.6c.4.5.3 1.1-.1 1.5L4.6 6.3c.9 2 2.5 3.7 4.6 4.7l1.1-1.1c.4-.4 1-.5 1.5-.1l2.6 2.1c.5.4.5 1.1.1 1.6l-1.3 1.3c-.6.6-1.5.8-2.3.5C6 13.8 2.3 10.1.9 5.1.7 4.3.9 3.4 1.5 2.8l.6-.6c.4-.4 1.1-.5 1.5 0z"/></svg>
        </li>
        <li>555-555-0192
          <svg viewBox="0 0 16 16" aria-hidden="true"><path d="M4 1h6l2 2v3H4z"/><path d="M1 7h14v6h-3v-2H4v2H1z"/><path d="M5 12h6v3H5z"/></svg>
        </li>
        <li>dale.hoskin@pellorvh.example
          <svg viewBox="0 0 16 16" aria-hidden="true"><path d="M1 3h14v1.5L8 9 1 4.5z"/><path d="M1 6.3l7 4.4 7-4.4V13H1z"/></svg>
        </li>
        <li>PellorValleyHospital.Example
          <svg viewBox="0 0 16 16" aria-hidden="true"><circle cx="8" cy="8" r="7"/><path d="M5 4c1.5 0 2 1 1.5 2S5 7 6 8.5s2 .5 2.5 2S8 13 8 13M10 3c0 1.5 1 1.5 2 2s1 2 2 2" stroke="#f3f3f3" stroke-width="1.2" fill="none"/></svg>
        </li>
      </ul>
    </div>
  </section>

  <section class="card card-back">
    <div class="wordmark">Pellor<br>Valley<br>Hospital</div>
    <p class="back-url">www.PellorValleyHospital.Example</p>
  </section>
</body>
</html>
```